Muddy Boots Pet Parlour

Design a flyer (A5 - I think!) with bright colours to promote an in home Dog Service.
Include an animated picture of a dog (being walked/playing/jumping etc)
Bold Heading, list of services with animated pictures, contact details

• Add price list to back of A5 Flyer with same colours and design as front page of flyer - See Attached.

```html
<!DOCTYPE html>
<html lang="en">
<head>
<meta charset="utf-8">
<title>Muddy Boots Pet Parlour – In Home Dog Services</title>
<link rel="stylesheet" href="https://fonts.googleapis.com/css2?family=Fredoka:wght@600;700&family=Josefin+Sans:wght@600;700&family=Montserrat:wght@800&display=swap">
<style>
  :root {
    --sun: #fbf0b0;
    --sun-light: #fffbe6;
    --board-dark: #6e2812;
    --board-light: #a8461e;
    --orange: #f46b0a;
    --orange-deep: #e05f08;
    --cream: #fcd57a;
    --cream-light: #fde3a0;
    --mint: #58efa0;
    --mint-dark: #22c878;
    --aqua-light: #d8fbf0;
    --aqua: #a8eef0;
    --ink: #141414;
    --white: #ffffff;
  }
  * { margin: 0; padding: 0; box-sizing: border-box; }
  html, body { width: 846px; height: 1200px; overflow: hidden; }
  body { background: var(--sun); }
  .flyer {
    position: relative; width: 846px; height: 1200px; overflow: hidden;
    background: repeating-linear-gradient(90deg, var(--sun) 0 24px, var(--sun-light) 24px 48px);
  }
  .board {
    position: absolute; left: 55px; top: 19px; width: 736px; height: 960px;
    border-radius: 46px 46px 0 0;
    background: radial-gradient(circle at 60% 60%, var(--board-light), var(--board-dark) 75%);
  }
  .banner {
    position: absolute; left: 11px; top: 72px; width: 824px; height: 70px;
    background: var(--mint); border-radius: 8px;
    box-shadow: 0 3px 0 var(--mint-dark);
    display: flex; align-items: center; justify-content: center;
  }
  .banner__title {
    font-family: "Josefin Sans", sans-serif; font-weight: 700;
    font-size: 44px; letter-spacing: 1px; color: var(--white);
    text-transform: uppercase; padding-top: 6px;
  }
  .service {
    position: absolute; width: 332px; height: 244px;
    border-radius: 18px; overflow: hidden;
    background: var(--cream);
    box-shadow: 0 0 0 4px rgba(255,190,90,0.55);
  }
  .service__question {
    height: 152px; background: var(--orange);
    display: flex; align-items: center; justify-content: center; text-align: center;
    padding: 30px 16px 0;
    font-family: "Fredoka", sans-serif; font-weight: 700; font-size: 27px;
    line-height: 1.15; color: var(--white); text-transform: uppercase;
  }
  .service__answer {
    height: 92px; display: flex; align-items: center; justify-content: center; text-align: center;
    padding: 0 18px;
    background: linear-gradient(180deg, var(--cream), var(--cream-light));
    font-family: "Josefin Sans", sans-serif; font-weight: 600; font-size: 20px;
    line-height: 1.25; color: var(--ink); text-transform: uppercase;
  }
  .service::after {
    content: ""; position: absolute; inset: 8px;
    border: 2px dotted var(--white); border-radius: 12px; pointer-events: none;
  }
  .service--poop { left: 83px; top: 169px; }
  .service--walk { left: 436px; top: 169px; }
  .service--feed { left: 83px; top: 432px; }
  .service--play { left: 436px; top: 432px; }
  .service--bath { left: 83px; top: 708px; }
  .bone-tag {
    position: absolute; width: 140px; height: 40px; border-radius: 20px;
    background: var(--white); box-shadow: 0 2px 0 rgba(0,0,0,0.15);
  }
  .bone-tag--poop { left: 179px; top: 153px; }
  .bone-tag--walk { left: 532px; top: 153px; }
  .bone-tag--feed { left: 179px; top: 416px; }
  .bone-tag--play { left: 532px; top: 416px; }
  .bone-tag--bath { left: 179px; top: 692px; }
  .dog-illustration {
    position: absolute; left: 452px; top: 692px; width: 360px; height: 270px;
    border-radius: 40% 46% 22% 30% / 46% 50% 24% 26%;
    background: linear-gradient(160deg, var(--orange) 0%, var(--orange-deep) 100%);
  }
  .footer-wave { position: absolute; left: 0; top: 900px; width: 846px; height: 300px; }
  .footer-call {
    position: absolute; left: 0; top: 998px; width: 846px; text-align: center;
    font-family: "Montserrat", sans-serif; font-weight: 800; font-size: 22px;
    color: var(--ink); text-transform: uppercase; letter-spacing: 0.3px;
  }
  .footer-name {
    position: absolute; left: 0; top: 1056px; width: 846px; text-align: center;
    font-family: "Josefin Sans", sans-serif; font-weight: 600; font-size: 46px;
    color: var(--ink); text-transform: uppercase;
  }
  .footer-rule {
    position: absolute; left: 95px; top: 1122px; width: 656px;
    border-top: 5px dotted rgba(120,220,210,0.8);
  }
  .footer-contact {
    position: absolute; left: 0; top: 1146px; width: 846px; text-align: center;
    font-family: "Josefin Sans", sans-serif; font-weight: 600; color: var(--ink);
  }
  .footer-contact__phone { font-size: 38px; }
  .footer-contact__sep { font-size: 28px; margin: 0 8px; }
  .footer-contact__web { font-size: 29px; }
</style>
</head>
<body>
<main class="flyer">
  <div class="board"></div>

  <header class="banner">
    <h1 class="banner__title">Muddy Boots Pet Parlour</h1>
  </header>

  <section class="service service--poop">
    <h2 class="service__question">Tired of<br>picking up<br>dog poop?</h2>
    <p class="service__answer">Arrange for us<br>to do it for you!</p>
  </section>
  <section class="service service--walk">
    <h2 class="service__question">Need a break<br>from walking<br>the dog?</h2>
    <p class="service__answer">We will come and<br>collect your dog and<br>take it for a walk!</p>
  </section>
  <section class="service service--feed">
    <h2 class="service__question">Can’t get<br>home in time<br>to feed<br>our dog?</h2>
    <p class="service__answer">Use our dog feeding<br>service!</p>
  </section>
  <section class="service service--play">
    <h2 class="service__question">Want someone to<br>play with your<br>dog while you’re<br>at work?</h2>
    <p class="service__answer">Muddy Boots Pet<br>Parlour is here!</p>
  </section>
  <section class="service service--bath">
    <h2 class="service__question">Dog<br>needs<br>a bath?</h2>
    <p class="service__answer">We’ll arrange for a<br>professional to<br>keep it clean!</p>
  </section>

  <div class="bone-tag bone-tag--poop" role="img" aria-label="Bone shaped tag"></div>
  <div class="bone-tag bone-tag--walk" role="img" aria-label="Bone shaped tag"></div>
  <div class="bone-tag bone-tag--feed" role="img" aria-label="Bone shaped tag"></div>
  <div class="bone-tag bone-tag--play" role="img" aria-label="Bone shaped tag"></div>
  <div class="bone-tag bone-tag--bath" role="img" aria-label="Bone shaped tag"></div>

  <div class="dog-illustration" role="img" aria-label="Cartoon orange dog with a green collar carrying a red frisbee"></div>

  <svg class="footer-wave" viewBox="0 0 846 300" aria-hidden="true">
    <defs>
      <linearGradient id="footer-fill" x1="0" y1="0" x2="0" y2="1">
        <stop offset="0" stop-color="#d8fbf0"/>
        <stop offset="1" stop-color="#a8eef0"/>
      </linearGradient>
    </defs>
    <path d="M0 12 Q423 110 846 12 L846 300 L0 300 Z" fill="url(#footer-fill)"/>
    <path d="M0 12 Q423 110 846 12" fill="none" stroke="#58efa0" stroke-width="5"/>
    <path d="M0 26 Q423 124 846 26" fill="none" stroke="#58efa0" stroke-width="4" stroke-dasharray="2 8" stroke-linecap="round"/>
  </svg>

  <p class="footer-call">For all services related to your dog – call MBPP</p>
  <p class="footer-name">“Muddy Boots Pet Parlour”</p>
  <div class="footer-rule"></div>
  <p class="footer-contact">
    <span class="footer-contact__phone">0400 518 342</span><span class="footer-contact__sep">|</span><span class="footer-contact__web">www.muddybootspetparlour.com.au</span>
  </p>
</main>
</body>
</html>
```